Outdoor Company Business Card design

We are an outdoor adventure company needing a business card. We sell outdoor adventures and clothing. Please use our logo in the business card. We are looking for something unique but delivers a clear message as to who we are. Please be creative

Target Market(s)

Outdoor adventures

Industry/Entity Type

Business

Contact Information for Business Card

Business name: TrailBrook If using the logo, no need to have a spot for the name
Owner / CEO: Owen Pardle
Website: TrailBrook.example
Facebook: Facebook.com/TrailBrook
Instagram: @pardle_owen
phone number: 555-384-7120
Email: Pardleteams@TrailBrook.example

Colors

Designer to choose colors to be used in the design.

Requirements
Must have
• The business card must include the details mentioned above. ie logo, my name, email, facebook, instagram, website, and phone number.
Should not have
• should not be cluttered or look messy

```html
<!DOCTYPE html>
<html lang="en">
<head>
<meta charset="utf-8">
<title>TrailBrook Business Card</title>
<link rel="stylesheet" href="https://fonts.googleapis.com/css2?family=Lato:wght@300;400;700&display=swap">
<style>
  :root {
    --canvas: #757575;
    --card-dark: #262626;
    --card-dark-edge: #1d1d1d;
    --card-light: #ffffff;
    --brand-blue: #0f72b8;
    --brand-orange: #ea5726;
    --ink: #2f2f2f;
    --muted-white: #e8e8e8;
  }
  * { box-sizing: border-box; margin: 0; padding: 0; }
  html, body { width: 1058px; height: 1200px; overflow: hidden; }
  body {
    background: var(--canvas);
    font-family: "Lato", sans-serif;
    display: flex;
    flex-direction: column;
    justify-content: space-evenly;
    align-items: center;
  }
  .card {
    position: relative;
    width: 900px;
    height: 513px;
    overflow: hidden;
  }
  /* Back side */
  .card--back {
    background: linear-gradient(135deg, var(--card-dark) 0%, var(--card-dark-edge) 100%);
  }
  .back-brand {
    position: absolute;
    top: 270px;
    left: 0;
    width: 100%;
    text-align: center;
  }
  .brand-name {
    font-weight: 700;
    color: var(--brand-blue);
    letter-spacing: 1px;
    display: inline-flex;
    align-items: center;
    gap: 14px;
  }
  .brand-name .brand-dot {
    display: inline-block;
    border-radius: 50%;
    background: var(--brand-orange);
  }
  .back-brand .brand-name { font-size: 64px; }
  .back-brand .brand-dot { width: 22px; height: 22px; }
  .back-web {
    position: absolute;
    top: 422px;
    left: 0;
    width: 100%;
    text-align: center;
    font-size: 17px;
    letter-spacing: 2.5px;
    color: var(--muted-white);
  }
  .back-web strong { font-weight: 700; }

  /* Front side */
  .card--front { background: var(--card-light); }
  .holder {
    position: absolute;
    left: 86px;
    top: 108px;
  }
  .holder-name {
    font-weight: 300;
    font-size: 31px;
    color: var(--ink);
    line-height: 1.1;
  }
  .holder-role {
    font-weight: 700;
    font-size: 20px;
    color: var(--brand-blue);
  }
  .front-brand {
    position: absolute;
    right: 68px;
    top: 136px;
  }
  .front-brand .brand-name { font-size: 48px; }
  .front-brand .brand-dot { width: 16px; height: 16px; }
  .contact-list {
    position: absolute;
    left: 86px;
    top: 274px;
    list-style: none;
  }
  .contact-list li {
    display: flex;
    align-items: center;
    gap: 12px;
    font-size: 18px;
    line-height: 24px;
    color: var(--ink);
  }
  .contact-icon { width: 16px; height: 16px; flex: none; }
  .band {
    position: absolute;
    left: 0;
    top: 404px;
    width: 100%;
    height: 72px;
    background: var(--brand-blue);
  }
  .band-accent {
    position: absolute;
    right: 0;
    top: 0;
    width: 64px;
    height: 100%;
    background: var(--brand-orange);
  }
  .band-web {
    position: absolute;
    left: 86px;
    top: 50%;
    transform: translateY(-50%);
    font-size: 18px;
    color: #fff;
  }
  .band-web strong { font-weight: 700; }
</style>
</head>
<body>
  <section class="card card--back" aria-label="Card back">
    <div class="back-brand">
      <span class="brand-name"><span class="brand-dot"></span>TrailBrook</span>
    </div>
    <p class="back-web">www.<strong>TrailBrook</strong>.example</p>
  </section>

  <section class="card card--front" aria-label="Card front">
    <div class="holder">
      <p class="holder-name">Owen Pardle</p>
      <p class="holder-role">Owner / CEO</p>
    </div>

    <div class="front-brand">
      <span class="brand-name"><span class="brand-dot"></span>TrailBrook</span>
    </div>

    <ul class="contact-list">
      <li>
        <svg class="contact-icon" viewBox="0 0 16 16" aria-hidden="true">
          <rect x="4" y="1" width="8" height="14" rx="1.5" fill="none" stroke="#ea5726" stroke-width="1.8"/>
          <circle cx="8" cy="12.3" r="0.9" fill="#ea5726"/>
        </svg>
        555-384-7120
      </li>
      <li>
        <svg class="contact-icon" viewBox="0 0 16 16" aria-hidden="true">
          <rect x="1.5" y="4" width="13" height="9" rx="1" fill="none" stroke="#ea5726" stroke-width="1.6"/>
          <path d="M1.8 4.5 L8 9 L14.2 4.5" fill="none" stroke="#ea5726" stroke-width="1.6"/>
        </svg>
        Pardleteams@TrailBrook.example
      </li>
      <li>
        <svg class="contact-icon" viewBox="0 0 16 16" aria-hidden="true">
          <circle cx="8" cy="8" r="7" fill="#ea5726"/>
        </svg>
        /TrailBrook
      </li>
      <li>
        <svg class="contact-icon" viewBox="0 0 16 16" aria-hidden="true">
          <circle cx="8" cy="8" r="7" fill="#ea5726"/>
        </svg>
        @pardle_owen
      </li>
    </ul>

    <div class="band">
      <p class="band-web"><strong>TrailBrook</strong>.example</p>
      <div class="band-accent"></div>
    </div>
  </section>
</body>
</html>
```